Velmora Builders LLC- Bus. Cards, Door Hangers, Invoice, Estimates, Postcards
I want a proffessional package that express who we are and what we do. www.velmora-builders.example
Velmora Builders LLC- Bus. Cards, Door Hangers, Invoice, Estimates, Postcards - Construction
Creative Brief
Professional
Calvin Tressel
Owner
4216 Pellham Ave. Denver, CO. 80417
calvin@velmora-builders.example
www.velmora-builders.example
Spray Foam Insulation Energy Auditing Weatherization Thermal Imaging

```html
<!DOCTYPE html>
<html lang="en">
<head>
<meta charset="utf-8">
<title>Velmora Builders – Business Card</title>
<link href="https://fonts.googleapis.com/css2?family=Mulish:wght@400;500;600;700&display=swap" rel="stylesheet">
<style>
  :root {
    --green-light: #8fd43c;
    --green-mid: #4fae2c;
    --green-dark: #22841a;
    --swoosh-grey: #3e3e3e;
    --ink: #1c1c1c;
    --muted: #5a5a5a;
    --paper: #ffffff;
    --frame: #9a9a9a;
  }
  html, body {
    margin: 0;
    padding: 0;
    width: 1200px;
    height: 698px;
    overflow: hidden;
    background: var(--paper);
  }
  .card {
    position: relative;
    width: 1200px;
    height: 698px;
    box-sizing: border-box;
    border: 2px solid var(--frame);
    background: var(--paper);
    font-family: "Mulish", "Helvetica Neue", Arial, sans-serif;
    color: var(--ink);
    overflow: hidden;
  }
  .card__swooshes {
    position: absolute;
    inset: 0;
    width: 100%;
    height: 100%;
  }
  .holder {
    position: absolute;
    top: 60px;
    right: 46px;
    text-align: right;
  }
  .holder__name {
    margin: 0;
    font-size: 26px;
    font-weight: 700;
    line-height: 1.25;
  }
  .holder__title {
    margin: 0;
    font-size: 25px;
    font-weight: 400;
    line-height: 1.3;
  }
  .brand {
    position: absolute;
    top: 322px;
    left: 0;
    width: 100%;
    text-align: center;
  }
  .brand__lockup {
    display: inline-flex;
    align-items: center;
    gap: 16px;
  }
  .brand__dot {
    width: 40px;
    height: 40px;
    border-radius: 50%;
    background: var(--green-mid);
  }
  .brand__name {
    font-size: 56px;
    font-weight: 600;
    color: var(--green-mid);
    letter-spacing: -0.5px;
    line-height: 1;
  }
  .brand__tagline {
    margin: 14px 0 0;
    font-size: 12.5px;
    font-weight: 700;
    letter-spacing: 1.4px;
    color: var(--muted);
  }
  .contact {
    position: absolute;
    left: 34px;
    top: 498px;
    margin: 0;
    padding: 0;
    list-style: none;
    font-size: 27px;
    line-height: 34px;
  }
  .contact__label {
    display: inline-block;
    width: 40px;
  }
</style>
</head>
<body>
<div class="card">
  <svg class="card__swooshes" viewBox="0 0 1200 698" aria-hidden="true">
    <defs>
      <radialGradient id="greenTop" cx="0.4" cy="0.3" r="0.7">
        <stop offset="0" stop-color="var(--green-light)"/>
        <stop offset="1" stop-color="var(--green-dark)"/>
      </radialGradient>
      <radialGradient id="greenBottom" cx="0.75" cy="0.7" r="0.6">
        <stop offset="0" stop-color="var(--green-light)"/>
        <stop offset="1" stop-color="var(--green-dark)"/>
      </radialGradient>
    </defs>
    <path d="M0,0 H900 C560,30 200,170 0,472 Z" fill="var(--swoosh-grey)"/>
    <path d="M0,0 H870 C530,24 180,150 0,446 Z" fill="url(#greenTop)"/>
    <path d="M620,698 C860,610 1060,500 1200,384 V698 Z" fill="var(--swoosh-grey)"/>
    <path d="M650,698 C880,622 1070,520 1200,408 V698 Z" fill="url(#greenBottom)"/>
  </svg>

  <div class="holder">
    <p class="holder__name">Calvin Tressel</p>
    <p class="holder__title">Owner</p>
  </div>

  <div class="brand">
    <div class="brand__lockup">
      <span class="brand__dot"></span>
      <span class="brand__name">Velmora Builders</span>
    </div>
    <p class="brand__tagline">Crafting Comfort And Lasting Savings For Homes</p>
  </div>

  <ul class="contact">
    <li>4216 Pellham Ave. Denver, CO. 80417</li>
    <li><span class="contact__label">P</span>:&nbsp; 631-555-0148</li>
    <li><span class="contact__label">E</span>:&nbsp; calvin@velmora-builders.example</li>
    <li><span class="contact__label">W</span>:&nbsp; www.velmora-builders.example</li>
  </ul>
</div>
</body>
</html>
```